Business Card Design

We need a business card design for a new company located in Missouri City, TX, entitled 'Brightmere Chiropractic & Holistic Center'. Our services include restoration of health and vitality, spinal exam, health assessment, dietary & fitness programs, lymphatic & therapeutic massage, detox & remineralize body wraps, far infrared sauna therapy

Industry/Entity Type

Business

Contact Information for Business Card

Brightmere Chiropractic & Holistic Center, Marlena Voss LMT, 4125 Hwy. 9, Suite 300, Missouri City, TX 77312, 281-555-0193

```html
<!DOCTYPE html>
<html lang="en">
<head>
<meta charset="utf-8">
<title>Brightmere Chiropractic &amp; Holistic Center – Business Card</title>
<link rel="stylesheet" href="https://fonts.googleapis.com/css2?family=Old+Standard+TT:wght@400;700&family=Open+Sans:wght@400;600&display=swap">
<style>
  :root {
    --backdrop: #2f2a27;
    --card: #1e1e1e;
    --card-edge: #2a2a2a;
    --teal: #1ba38e;
    --teal-soft: #179884;
    --blue: #2c6aa3;
    --white: #f4f4f4;
    --muted: #d8d8d8;
  }
  * { box-sizing: border-box; margin: 0; padding: 0; }
  html, body {
    width: 1200px; height: 780px; overflow: hidden;
    background: var(--backdrop);
  }
  .stage {
    width: 1200px; height: 780px;
    display: flex; align-items: center; justify-content: center; gap: 40px;
  }
  .card {
    width: 550px; height: 314px;
    background: var(--card);
    border: 1px solid var(--card-edge);
    border-radius: 4px;
    position: relative;
    overflow: hidden;
  }

  /* Front */
  .card--front { display: flex; }
  .brand {
    width: 218px;
    display: flex; flex-direction: column; justify-content: flex-end;
    padding: 0 18px 58px 26px;
    border-right: 1.5px solid var(--blue);
    margin: 24px 0 24px 0;
  }
  .brand__name {
    display: flex; align-items: center; gap: 10px;
    font-family: "Old Standard TT", serif; font-weight: 400;
    font-size: 30px; color: var(--white); line-height: 1;
  }
  .brand__dot {
    width: 14px; height: 14px; border-radius: 50%;
    background: var(--teal); flex: none;
  }
  .brand__tagline {
    margin-top: 8px;
    font-family: "Open Sans", sans-serif; font-size: 12.5px; color: var(--white);
    white-space: nowrap;
  }
  .details { padding: 30px 20px 0 22px; flex: 1; }
  .person__name {
    font-family: "Old Standard TT", serif; font-size: 28px; color: var(--teal);
    line-height: 1.05;
  }
  .person__title {
    font-family: "Old Standard TT", serif; font-size: 14px; color: var(--white);
    margin-top: 2px;
  }
  .contact { list-style: none; margin-top: 36px; }
  .contact__item {
    display: flex; align-items: flex-start; gap: 9px;
    font-family: "Open Sans", sans-serif; font-size: 13px; color: var(--white);
    line-height: 1.45; margin-bottom: 3px;
  }
  .contact__icon {
    width: 13px; height: 13px; flex: none; margin-top: 3px;
  }

  /* Back */
  .card--back { padding: 40px 30px 0; }
  .services__heading {
    display: flex; align-items: center; gap: 12px;
    font-family: "Old Standard TT", serif; font-weight: 700;
    font-size: 32px; color: var(--white);
  }
  .services__heading::before,
  .services__heading::after {
    content: ""; flex: 1; height: 1.5px; background: var(--teal);
  }
  .services__list {
    list-style: none; text-align: center; margin-top: 8px;
    font-family: "Old Standard TT", serif; font-weight: 700;
    font-size: 21px; line-height: 29px; color: var(--teal-soft);
  }
</style>
</head>
<body>
<main class="stage">

  <section class="card card--front" aria-label="Business card front">
    <div class="brand">
      <div class="brand__name"><span class="brand__dot"></span>Brightmere</div>
      <div class="brand__tagline">Chiropractic &amp; Holistic Center</div>
    </div>
    <div class="details">
      <h1 class="person__name">Delia Hartwell</h1>
      <p class="person__title">Chief Executive</p>
      <ul class="contact">
        <li class="contact__item">
          <svg class="contact__icon" viewBox="0 0 13 13" aria-hidden="true"><rect width="13" height="13" rx="2" fill="var(--teal)"/><path d="M4 3.2l1.4 1.8-.8.9c.6 1.3 1.3 2 2.5 2.5l.9-.8 1.8 1.4-.7 1.1C6 10 3 7 2.9 3.9z" fill="#1e1e1e"/></svg>
          <span>281-555-0193</span>
        </li>
        <li class="contact__item">
          <svg class="contact__icon" viewBox="0 0 13 13" aria-hidden="true"><rect width="13" height="13" rx="2" fill="var(--teal)"/><rect x="2.5" y="3.8" width="8" height="5.4" fill="#1e1e1e"/><path d="M2.5 3.8l4 3 4-3" stroke="var(--teal)" fill="none"/></svg>
          <span>delia.hartwell@brightmere.example</span>
        </li>
        <li class="contact__item">
          <svg class="contact__icon" viewBox="0 0 13 13" aria-hidden="true"><rect width="13" height="13" rx="2" fill="var(--teal)"/><circle cx="6.5" cy="6.5" r="3.6" fill="none" stroke="#1e1e1e" stroke-width="1.1"/><path d="M2.9 6.5h7.2M6.5 2.9c-1.6 2-1.6 5.2 0 7.2M6.5 2.9c1.6 2 1.6 5.2 0 7.2" stroke="#1e1e1e" stroke-width=".8" fill="none"/></svg>
          <span>www.brightmere.example</span>
        </li>
        <li class="contact__item">
          <svg class="contact__icon" viewBox="0 0 13 13" aria-hidden="true"><rect width="13" height="13" rx="2" fill="var(--teal)"/><path d="M6.5 10.8S3.4 7.6 3.4 5.4a3.1 3.1 0 016.2 0c0 2.2-3.1 5.4-3.1 5.4z" fill="#1e1e1e"/><circle cx="6.5" cy="5.3" r="1.1" fill="var(--teal)"/></svg>
          <span>Marlena Voss LMT, 4125 Hwy. 9, Suite 300, Missouri City, TX 77312,</span>
        </li>
      </ul>
    </div>
  </section>

  <section class="card card--back" aria-label="Business card back">
    <h2 class="services__heading">Services</h2>
    <ul class="services__list">
      <li>restoration of health and vitality</li>
      <li>spinal exam</li>
      <li>health assessment</li>
      <li>dietary &amp; fitness programs</li>
      <li>lymphatic &amp; therapeutic massage</li>
      <li>detox &amp; remineralize body wraps</li>
      <li>far infrared sauna therapy</li>
    </ul>
  </section>

</main>
</body>
</html>
```